KVT Social Media Graphics (Square)

Use the following images and headlines to create 7 individual social media graphics (square size); You can mix and match the text that's there to create different social media graphics. Note: each graphic should have one of the pictures of the bottle on it and/or one of the images with a person on it (pics attached to the brief)

Target Market(s)

women and men who are overweight looking for fast, healthy weight loss

Industry/Entity Type

health and wellness

Colors
0054AA
0677BA
7BADD7
CADEEF
E8F1F8

Requirements
Must have
• Use color scheme that's complimentary to the blood sugar bottle
Nice to have
• the text provided in the WORD document

```html
<!DOCTYPE html>
<html lang="en">
<head>
<meta charset="utf-8">
<title>KVT – Boost GLP-1 Levels And Support Fat Loss</title>
<link href="https://fonts.googleapis.com/css2?family=Outfit:wght@500;600;700;800&display=swap" rel="stylesheet">
<style>
  :root {
    --blue-top: #1060ff;
    --blue-deep: #3f2dff;
    --ink-blue: #1f3fd6;
    --accent-yellow: #ffb800;
    --white: #ffffff;
    --rim-grey: #c9c9cf;
    --pill-start: #2a4cff;
    --pill-end: #4c3cff;
  }
  * { margin: 0; padding: 0; box-sizing: border-box; }
  html, body { width: 1200px; height: 1200px; overflow: hidden; }
  body { font-family: "Outfit", sans-serif; }

  .social-tile {
    position: relative;
    width: 1200px;
    height: 1200px;
    overflow: hidden;
    background: linear-gradient(135deg, var(--blue-top) 0%, #2a4bff 45%, var(--blue-deep) 100%);
  }

  .wave-base { position: absolute; inset: 0; }

  .product-shot { position: absolute; left: 30px; top: 250px; width: 580px; height: 940px; }

  .headline {
    position: absolute;
    color: var(--white);
    font-weight: 700;
    font-size: 80px;
    line-height: 1;
    letter-spacing: -0.5px;
  }
  .headline-line1 { left: 143px; top: 140px; }
  .headline-line2 { left: 690px; top: 214px; }

  .divider-line {
    position: absolute;
    left: 628px;
    top: 323px;
    width: 3px;
    height: 244px;
    background: var(--accent-yellow);
  }

  .headline-accent {
    position: absolute;
    left: 686px;
    color: var(--accent-yellow);
    font-weight: 800;
    font-size: 148px;
    line-height: 1;
    letter-spacing: -2px;
  }
  .accent-fat { top: 303px; }
  .accent-loss { top: 433px; }

  .benefit-list {
    position: absolute;
    left: 575px;
    top: 772px;
    list-style: none;
    color: var(--ink-blue);
    font-weight: 500;
    font-size: 26px;
    line-height: 27px;
  }
  .benefit-list li {
    position: relative;
    padding-left: 33px;
    margin-bottom: 13px;
  }
  .benefit-list li::before {
    content: "";
    position: absolute;
    left: 4px;
    top: 8px;
    width: 11px;
    height: 11px;
    background: var(--ink-blue);
    transform: rotate(45deg) scaleY(1.3);
  }

  .pill {
    position: absolute;
    top: 1080px;
    height: 33px;
    border-radius: 17px;
    background: linear-gradient(90deg, var(--pill-start), var(--pill-end));
    color: var(--white);
    font-weight: 500;
    font-size: 20px;
    line-height: 33px;
    text-align: center;
  }
  .pill-supplement { left: 580px; width: 238px; }
  .pill-capsules { left: 836px; width: 290px; }
</style>
</head>
<body>
  <main class="social-tile">
    <svg class="wave-base" width="1200" height="1200" viewBox="0 0 1200 1200" aria-hidden="true">
      <defs>
        <radialGradient id="burstFade" cx="0.45" cy="0.55" r="0.7">
          <stop offset="0" stop-color="#ffffff"/>
          <stop offset="0.6" stop-color="#f3f3f5"/>
          <stop offset="1" stop-color="#e4e4e8"/>
        </radialGradient>
      </defs>
      <path d="M0 640 L560 640 C700 640 780 740 930 742 C1050 744 1130 700 1200 668 L1200 1200 L0 1200 Z" fill="var(--rim-grey)"/>
      <path d="M0 655 L560 655 C700 655 780 752 930 754 C1050 756 1130 714 1200 684 L1200 1200 L0 1200 Z" fill="url(#burstFade)"/>
    </svg>

    <svg class="product-shot" viewBox="0 0 580 940" role="img" aria-label="Product bottle of the KVT blood sugar dietary supplement, 60 vegetable capsules">
      <defs>
        <linearGradient id="bottleTone" x1="0" y1="0" x2="0" y2="1">
          <stop offset="0" stop-color="#f4f5f8"/>
          <stop offset="0.62" stop-color="#ffffff"/>
          <stop offset="0.78" stop-color="#3c3ca0"/>
          <stop offset="1" stop-color="#2a3fc8"/>
        </linearGradient>
      </defs>
      <g transform="rotate(8 290 470)">
        <rect x="195" y="20" width="330" height="180" rx="18" fill="#d2d4da"/>
        <rect x="80" y="185" width="470" height="720" rx="70" fill="url(#bottleTone)"/>
      </g>
    </svg>

    <h1 class="headline headline-line1">Boost GLP-1 Levels And</h1>
    <div class="headline headline-line2">Support</div>
    <div class="divider-line"></div>
    <div class="headline-accent accent-fat">Fat</div>
    <div class="headline-accent accent-loss">Loss</div>

    <ul class="benefit-list">
      <li>Increase GLP-1 Levels*</li>
      <li>Support Fat Loss*</li>
      <li>Reduce Cravings for<br>Sugar and Carbs*</li>
      <li>Feel Full Faster &amp;<br>Stay Full Longer*</li>
      <li>Support Healthy<br>Blood Sugar Levels*</li>
    </ul>

    <div class="pill pill-supplement">Dietary Supplement</div>
    <div class="pill pill-capsules">60 Vegetable Capsules</div>
  </main>
</body>
</html>
```